New Signage Design Project

Real estate company looking for signage, PowerPoint and stationery branding. Signs will be placed in front of homes and other properties being sold

Name of company is Birch Crest, LLC

Requirements
Must have
• Name of company - Birch Crest, LLC

```html
<!DOCTYPE html>
<html lang="en">
<head>
<meta charset="utf-8">
<title>Birch Crest, LLC — For Sale Sign</title>
<link href="https://fonts.googleapis.com/css2?family=Jost:wght@400;500;700&display=swap" rel="stylesheet">
<style>
  :root {
    --backdrop: #c4c4c4;
    --ink-dark: #0a1e1f;
    --paper: #ffffff;
    --paper-tint: #f6f7f7;
    --accent-red: #e04a58;
    --text-black: #0b0b0b;
    --silver-light: #f4f4f4;
    --silver-mid: #bdbdbd;
    --silver-dark: #9a9a9a;
  }
  * { margin: 0; padding: 0; box-sizing: border-box; }
  html, body {
    width: 1200px;
    height: 928px;
    overflow: hidden;
    background: var(--backdrop);
    font-family: "Jost", "Futura", sans-serif;
  }
  .sign {
    position: absolute;
    left: 50px;
    top: 74px;
    width: 1000px;
    height: 708px;
    transform: scale(1.1);
    transform-origin: top left;
    background: var(--paper);
    overflow: hidden;
  }
  .sign-header {
    position: absolute;
    left: 0; top: 0;
    width: 100%;
    height: 352px;
    background: var(--ink-dark);
  }
  .sign-body-tint {
    position: absolute;
    left: 0; top: 352px;
    width: 100%;
    height: 356px;
    background: var(--paper-tint);
  }
  .brand-lockup {
    position: absolute;
    left: 0; top: 100px;
    width: 100%;
    display: flex;
    justify-content: center;
    align-items: center;
    gap: 26px;
  }
  .brand-dot {
    width: 70px;
    height: 70px;
    border-radius: 50%;
    background: var(--accent-red);
  }
  .brand-name {
    color: var(--paper);
    font-weight: 700;
    font-size: 64px;
    line-height: 1;
    letter-spacing: 0.5px;
  }
  .sale-ribbon {
    position: absolute;
    left: 91px; top: 278px;
    width: 816px;
    height: 152px;
  }
  .sale-label {
    position: absolute;
    left: 0; top: 278px;
    width: 100%;
    height: 152px;
    display: flex;
    justify-content: center;
    align-items: center;
    font-weight: 400;
    font-size: 114px;
    letter-spacing: 4px;
    word-spacing: 16px;
    color: var(--text-black);
    line-height: 1;
  }
  .agent-name {
    position: absolute;
    left: 0; top: 456px;
    width: 100%;
    text-align: center;
    color: var(--accent-red);
    font-weight: 700;
    font-size: 70px;
    line-height: 1;
  }
  .contact-rule {
    position: absolute;
    left: 225px; top: 552px;
    width: 548px;
    height: 2px;
    background: linear-gradient(90deg, transparent, var(--ink-dark) 15%, var(--ink-dark) 85%, transparent);
  }
  .contact-phone {
    position: absolute;
    left: 0; top: 564px;
    width: 100%;
    text-align: center;
    color: var(--ink-dark);
    font-weight: 400;
    font-size: 62px;
    line-height: 1;
    letter-spacing: 1px;
  }
  .web-tab {
    position: absolute;
    left: 277px; top: 655px;
    width: 446px;
    height: 60px;
    background: var(--ink-dark);
    border-radius: 26px 26px 0 0;
    display: flex;
    justify-content: center;
    padding-top: 12px;
  }
  .web-address {
    color: var(--paper);
    font-size: 25px;
    letter-spacing: 2.5px;
    font-weight: 400;
  }
</style>
</head>
<body>
  <main class="sign">
    <div class="sign-header"></div>
    <div class="sign-body-tint" role="img" aria-label="Faint repeating brand pattern background"></div>

    <div class="brand-lockup">
      <span class="brand-dot"></span>
      <span class="brand-name">Birch Crest, LLC</span>
    </div>

    <svg class="sale-ribbon" viewBox="0 0 816 152" aria-hidden="true">
      <defs>
        <linearGradient id="silver" x1="0" y1="0" x2="1" y2="0">
          <stop offset="0" stop-color="var(--silver-dark)"/>
          <stop offset="0.25" stop-color="var(--silver-light)"/>
          <stop offset="0.45" stop-color="var(--silver-mid)"/>
          <stop offset="0.7" stop-color="var(--silver-light)"/>
          <stop offset="0.9" stop-color="var(--silver-mid)"/>
          <stop offset="1" stop-color="var(--silver-light)"/>
        </linearGradient>
      </defs>
      <polygon points="0,0 762,0 816,76 762,152 0,152 34,76" fill="url(#silver)"/>
    </svg>
    <div class="sale-label">FOR SALE</div>

    <div class="agent-name">Birch Crest, LLC</div>
    <div class="contact-rule"></div>
    <div class="contact-phone">0123 456 789</div>

    <div class="web-tab">
      <span class="web-address">www.birchcrestllc.com</span>
    </div>
  </main>
</body>
</html>
```